New high end server provider needs wordpress design

www.kv7hosting.com

Need a wordpress design for a high end server provider that provides overclocked dedicated servers for rent. We are located in Chicago but we have a presence is Virginia and Nevada for both our east and west coast customers.

We are a server provider that specializes in top end hardware with every feature designed for optimum performance. If it is not the best quality part or provides the best possible performance we don't run it. Our customers are mainly those that want the best single threaded performance possible from their hardware. We would be selling our services directly on our website via WHMCS.

We would like to see designs that are very modern and simplistic yet very attractive looking and catchy. Would prefer colors in the blues and greens and white. These colors are not necessary and I would be open to another color scheme if it looks good.

The final design should show speed and performance while being simplistic and easy on the eyes.

Logo and company name added and payment changed to guaranteed.  Looking for a wordpress template with the same pages as kv7hosting.com but with a redesigned look and feel.  

WHMCS control panel design also part of the design request.

If you have any questions please let me know!  This is just for kv7hosting.com and a main page for WHMCS (no coding just design).

Target Market(s)

IT Guru's (mostly men in their 20's to 30's)

Industry/Entity Type

Hardware

Requirements
Must have
• WHMCS panel design to fit with website theme.
Nice to have
• Main slider on home page similar to one of our other websites at www.kv7hosting.com
Should not have
• Flash or frames

```html
<!DOCTYPE html>
<html lang="en">
<head>
<meta charset="utf-8">
<title>KV7HOSTING – Only the Best Hosting Solutions</title>
<link href="https://fonts.googleapis.com/css2?family=PT+Sans+Narrow:wght@400;700&family=PT+Serif:ital,wght@0,400;0,700;1,400&display=swap" rel="stylesheet">
<style>
  :root {
    --admin-bg: #232323;
    --admin-text: #d8d8d8;
    --header-bg: #070707;
    --brand-red: #e0513b;
    --nav-text: #c9c9c9;
    --nav-sep: #3a3a3a;
    --hero-dark: #2f2f2f;
    --hero-mid: #4a4a4a;
    --page-bg: #f4f6f5;
    --slider-band: #dcdcdc;
    --dot-grey: #d0d0d0;
    --dot-green: #7cc242;
    --accent-green: #8cc63f;
    --sub-green: #5f9a34;
    --heading: #1d1d1d;
    --body-text: #3b3b3b;
    --card-bg: #fbfcfb;
  }
  * { margin: 0; padding: 0; box-sizing: border-box; }
  html, body { width: 1200px; height: 900px; overflow: hidden; }
  body {
    position: relative;
    background: var(--page-bg);
    font-family: "PT Sans Narrow", "Arial Narrow", sans-serif;
    color: var(--body-text);
  }

  /* Admin bar */
  .admin-bar {
    position: absolute; left: 0; top: 0; width: 1200px; height: 36px;
    background: var(--admin-bg);
    color: var(--admin-text);
    font-size: 12px;
    display: flex; align-items: center;
  }
  .admin-bar .item { display: flex; align-items: center; gap: 5px; padding: 0 9px; height: 100%; }
  .admin-bar .site-mark { width: 14px; height: 14px; border-radius: 50%; border: 2px solid #9a9a9a; }
  .admin-bar .right { margin-left: auto; }
  .admin-bar .avatar { width: 12px; height: 14px; background: #bfbfbf; }

  /* Header */
  .site-header {
    position: absolute; left: 0; top: 36px; width: 1200px; height: 64px;
    background: var(--header-bg);
  }
  .brand {
    position: absolute; left: 302px; top: 20px;
    display: flex; align-items: center; gap: 9px;
  }
  .brand .square { width: 22px; height: 22px; background: var(--brand-red); }
  .brand .name {
    font-size: 19px; font-weight: 700; color: var(--brand-red); letter-spacing: 0.3px;
  }
  .main-nav {
    position: absolute; left: 606px; top: 25px;
    display: flex; align-items: center;
    font-size: 9.5px; text-transform: uppercase; color: var(--nav-text);
  }
  .main-nav .link { padding: 0 8px; border-left: 1px solid var(--nav-sep); line-height: 16px; }
  .main-nav .home { border-left: 0; padding: 0 10px 0 2px; display: flex; }

  /* Hero slider */
  .hero {
    position: absolute; left: 0; top: 100px; width: 1200px; height: 393px;
    background: radial-gradient(ellipse at 50% 70%, var(--hero-mid) 0%, var(--hero-dark) 70%);
    text-align: center;
  }
  .hero-title {
    position: absolute; left: 0; width: 1186px; top: 58px;
    font-size: 39px; font-weight: 700; color: #fff;
    text-shadow: 0 2px 4px rgba(0,0,0,0.6);
  }
  .hero-sub {
    position: absolute; left: 0; width: 1186px; top: 112px;
    font-family: "PT Serif", Georgia, serif; font-size: 14px; color: #b8b8b8;
  }
  .hero-sub strong { color: var(--accent-green); }
  .hero-visual {
    position: absolute; left: 400px; top: 170px; width: 386px; height: 223px;
    background: linear-gradient(180deg, #8a8a8a 0%, #2a2a2a 60%, #d8d8d8 100%);
    border-radius: 4px 4px 0 0;
  }
  .slider-bar {
    position: absolute; left: 180px; top: 493px; width: 830px; height: 40px;
    background: linear-gradient(90deg, rgba(220,220,220,0) 0%, var(--slider-band) 15%, var(--slider-band) 85%, rgba(220,220,220,0) 100%);
  }
  .slider-bar .arrow { position: absolute; top: 12px; }
  .slider-bar .prev { left: 120px; }
  .slider-bar .next { left: 696px; }
  .slider-dots { position: absolute; left: 386px; top: 17px; display: flex; gap: 3px; }
  .slider-dots span { width: 9px; height: 9px; border-radius: 50%; background: var(--dot-grey); border: 1px solid #bdbdbd; }
  .slider-dots .active { background: var(--dot-green); border-color: #5ea02c; }

  /* Features */
  .feature-card {
    position: absolute; left: 492px; top: 590px; width: 202px; height: 230px;
    background: var(--card-bg);
    box-shadow: 0 0 14px rgba(0,0,0,0.06);
  }
  .feature { position: absolute; top: 659px; width: 180px; }
  .feature h2 { font-size: 18px; font-weight: 700; color: var(--heading); text-align: center; text-transform: uppercase; }
  .feature h3 {
    font-family: "PT Serif", Georgia, serif; font-weight: 400; font-size: 12.5px;
    color: var(--sub-green); text-align: center; margin-top: 3px;
  }
  .feature p { font-size: 10.5px; line-height: 19px; margin-top: 17px; }
  .feature-speed { left: 299px; }
  .feature-secure { left: 502px; }
  .feature-support { left: 706px; }

  /* Call to action */
  .cta-note {
    position: absolute; top: 878px;
    font-family: "PT Serif", Georgia, serif; font-style: italic; font-size: 11.5px;
    color: var(--brand-red);
  }
  .cta-join { left: 323px; }
  .cta-learn { left: 732px; }
  .cta-button {
    position: absolute; left: 505px; top: 857px; width: 183px; height: 60px;
    background: var(--brand-red);
    box-shadow: 0 2px 4px rgba(0,0,0,0.25);
    color: #fff; font-size: 21px; text-align: center; padding-top: 16px;
  }
</style>
</head>
<body>
  <div class="admin-bar">
    <div class="item"><span class="site-mark"></span></div>
    <div class="item">kv7hosting</div>
    <div class="item">
      <svg width="11" height="11" viewBox="0 0 11 11"><path d="M1 1h9v6H5l-3 3V7H1z" fill="#9a9a9a"/></svg>
    </div>
    <div class="item">
      <svg width="10" height="10" viewBox="0 0 10 10"><path d="M4 0h2v4h4v2H6v4H4V6H0V4h4z" fill="#bdbdbd"/></svg>New
    </div>
    <div class="item">Edit Page</div>
    <div class="item right">Howdy, admin <span class="avatar"></span></div>
    <div class="item">
      <svg width="11" height="11" viewBox="0 0 11 11"><circle cx="4.5" cy="4.5" r="3.3" fill="none" stroke="#bdbdbd" stroke-width="1.6"/><path d="M7 7l3 3" stroke="#bdbdbd" stroke-width="1.8"/></svg>
    </div>
  </div>

  <header class="site-header">
    <div class="brand"><span class="square"></span><span class="name">KV7HOSTING</span></div>
    <nav class="main-nav">
      <span class="home">
        <svg width="10" height="10" viewBox="0 0 10 10"><path d="M5 0l5 5H8.5v5h-2V7h-3v3h-2V5H0z" fill="#fff"/></svg>
      </span>
      <span class="link">Solutions</span>
      <span class="link">Plans &amp; Pricing</span>
      <span class="link">Pages</span>
      <span class="link">Support</span>
      <span class="link">Contact</span>
    </nav>
  </header>

  <section class="hero">
    <h1 class="hero-title">Only the Best HOSTING Solutions</h1>
    <p class="hero-sub">We provide <strong>Fast &amp; Reliable</strong> hosting servers around the world</p>
    <div class="hero-visual" role="img" aria-label="Three tower servers standing side by side"></div>
  </section>

  <div class="slider-bar">
    <svg class="arrow prev" width="10" height="16" viewBox="0 0 10 16"><path d="M8 1L2 8l6 7" fill="none" stroke="#999" stroke-width="2"/></svg>
    <div class="slider-dots"><span class="active"></span><span></span><span></span><span></span><span class="active"></span></div>
    <svg class="arrow next" width="10" height="16" viewBox="0 0 10 16"><path d="M2 1l6 7-6 7" fill="none" stroke="#999" stroke-width="2"/></svg>
  </div>

  <div class="feature-card"></div>

  <article class="feature feature-speed">
    <h2>100MB/S Connection</h2>
    <h3>Connected to datacentre backbone</h3>
    <p>Our web servers are all connected to these 100 Mbps ports, which is then connected to the datacentre backbone, capable of up to the cool 90 Gb per second bandwidth!</p>
  </article>

  <article class="feature feature-secure">
    <h2>Secure &amp; Reliable</h2>
    <h3>Protected with UPS &amp; generators</h3>
    <p>In addition to high physical security, all servers are protected with UPS and backup generators, you just can't beat this affordable peace of mind lorem ipsum dolor sit amet!</p>
  </article>

  <article class="feature feature-support">
    <h2>24H Client Support</h2>
    <h3>No question is too stupid</h3>
    <p>Support directly from us, located in the UK, on a personal level with a friendly touch. There's no question too stupid or too clueless to ask lorem ipsum dolor mogrosit.</p>
  </article>

  <span class="cta-note cta-join">Already convinced? Join us here:</span>
  <div class="cta-button">SIGN UP FOR A PLAN</div>
  <span class="cta-note cta-learn">Not yet convinced? Learn more!</span>
</body>
</html>
```